New business card with our logo

we finalized our logo with the help of pixel harbor - now we need a business card using that logo. we are a metal service center providing raw steel and metal products for fabricating, contractors, artists, etc. we have the wording for the back of the card figured out (attached, no deviations from text please), just need help putting it all together.
would like the look of steel somehow incorporated in the design ... would like the black part of the logo to be steel or silver color (the S & BRANLEY)
Other font styles liked:
- calibri, arial, similar to those, modern looking
Colors
Designer to choose colors to be used in the design.
Requirements
Must have
- Back of card must haves are attached (no deviations from wording please).
- FRONT of card:
- logo
- address
- name
- office tel
- cell
- fax
- website
- address
Nice to have
- incorporate the look of steel or element of steel somehow
- names of the staff on front not in all caps, i.e. Rosvita not ROSVITA
- this industry is more industrial, not coffee or flower shop so design should be aligned with that
- design should be classic and tasteful

```html
<!DOCTYPE html>
<html lang="en">
<head>
<meta charset="utf-8">
<title>Branley Steel – Business Card</title>
<link rel="stylesheet" href="https://fonts.googleapis.com/css2?family=Lato:wght@400;700&family=Roboto:wght@400;500;700&display=swap">
<style>
  :root {
    --steel-blue: #0a70b8;
    --ink: #2b2b2b;
    --grey-text: #7a7a7a;
    --swoosh-grey: #8f9092;
    --faint-ring: #e3e8f2;
    --paper: #ffffff;
    --backdrop: #d8d6d3;
  }
  * { margin: 0; padding: 0; box-sizing: border-box; }
  html, body { width: 1200px; height: 849px; overflow: hidden; background: var(--backdrop); }
  .stage { position: relative; width: 1200px; height: 849px; }

  .card { position: absolute; left: 262px; width: 653px; overflow: hidden; box-shadow: 0 4px 14px rgba(0,0,0,.25); }

  /* Back of card */
  .card-back { top: 46px; height: 354px; background: var(--steel-blue); color: var(--paper); font-family: "Lato", sans-serif; }
  .card-back .brand { position: absolute; left: 72px; top: 40px; height: 112px; display: flex; align-items: center; gap: 24px; }
  .card-back .brand-dot { width: 112px; height: 112px; border: 6px solid var(--paper); border-radius: 50%; flex: none; }
  .card-back .brand-name { font-family: "Roboto", sans-serif; font-weight: 700; font-size: 49px; letter-spacing: 0.3px; line-height: 1; white-space: nowrap; }
  .card-back .services { position: absolute; left: 0; right: 0; top: 187px; text-align: center; }
  .card-back .headline { font-weight: 700; font-size: 31px; line-height: 34px; }
  .card-back .processes { font-size: 20.5px; line-height: 24px; }
  .card-back .products { position: absolute; left: 0; right: 0; top: 272px; text-align: center; font-size: 20.5px; line-height: 23.5px; }

  /* Front of card */
  .card-front { top: 446px; height: 356px; background: var(--paper); font-family: "Roboto", sans-serif; }
  .card-front .ring-deco { position: absolute; left: 422px; top: 162px; width: 224px; height: 224px; border: 13px solid var(--faint-ring); border-radius: 50%; }
  .card-front .brand { position: absolute; left: 42px; top: 35px; height: 64px; display: flex; align-items: center; gap: 14px; }
  .card-front .brand-dot { width: 64px; height: 64px; border: 5px solid var(--steel-blue); border-radius: 50%; flex: none; }
  .card-front .brand-name { font-weight: 700; font-size: 29px; color: var(--ink); line-height: 1; letter-spacing: 0.2px; white-space: nowrap; }
  .card-front .person { position: absolute; right: 40px; top: 62px; text-align: right; }
  .card-front .person-name { font-weight: 700; font-size: 26px; color: var(--steel-blue); line-height: 28px; }
  .card-front .person-title { font-size: 15.5px; color: var(--grey-text); line-height: 20px; margin-top: 1px; }
  .card-front .accent-bar { position: absolute; right: 0; top: 64px; width: 13px; height: 46px; background: var(--steel-blue); }
  .card-front .address { position: absolute; left: 42px; top: 160px; font-size: 15px; line-height: 20px; color: var(--grey-text); font-style: normal; }
  .card-front .contacts { position: absolute; left: 42px; top: 207px; list-style: none; font-size: 15px; color: var(--grey-text); }
  .card-front .contacts li { display: flex; align-items: center; height: 20px; gap: 10px; }
  .card-front .contacts svg { width: 11px; height: 11px; fill: var(--steel-blue); }
  .card-front .wave { position: absolute; left: 0; bottom: 0; width: 653px; height: 110px; }
  .card-front .website { position: absolute; left: 42px; top: 322px; font-size: 15.5px; color: var(--paper); }
</style>
</head>
<body>
<main class="stage">

  <section class="card card-back" aria-label="Back of card">
    <div class="brand">
      <span class="brand-dot"></span>
      <span class="brand-name">BRANLEY STEEL</span>
    </div>
    <div class="services">
      <p class="headline">Metal Service Center</p>
      <p class="processes">Cut • Shear • Punch • Light Fab</p>
    </div>
    <div class="products">
      <p>• Structural Steel • Stainless &amp; Aluminium</p>
      <p>• Building Components • Rebar • Decking......... and more!</p>
    </div>
  </section>

  <section class="card card-front" aria-label="Front of card">
    <span class="ring-deco"></span>
    <div class="brand">
      <span class="brand-dot"></span>
      <span class="brand-name">BRANLEY STEEL</span>
    </div>
    <div class="person">
      <p class="person-name">Corwin Hale</p>
      <p class="person-title">Managing Director</p>
    </div>
    <span class="accent-bar"></span>
    <address class="address">Rue Tallard 18<br>Hamilton 2040, Canada</address>
    <ul class="contacts">
      <li><svg viewBox="0 0 10 10"><path d="M2 0h6v10H2z M3 1v7h4V1z" fill-rule="evenodd"/></svg>+000 000 0000</li>
      <li><svg viewBox="0 0 10 10"><path d="M2 9C0 7 0 3 3 1l2 2-2 1c0 1 1 3 2 3l1-2 2 2C6 10 4 10 2 9z"/></svg>+000 000 0000</li>
      <li><svg viewBox="0 0 10 10"><path d="M2 0h6v3h2v5H8v2H2V8H0V3h2zM3 1v2h4V1zM3 6v3h4V6z" fill-rule="evenodd"/></svg>+000 000 0000</li>
      <li><svg viewBox="0 0 10 10"><path d="M0 2h10v1L5 6 0 3zM0 4l5 3 5-3v4H0z"/></svg>info@branleysteel.com</li>
    </ul>
    <svg class="wave" viewBox="0 246 653 110" preserveAspectRatio="none" aria-hidden="true">
      <path fill="var(--swoosh-grey)" d="M0,302 C130,266 270,290 410,326 C510,350 600,342 653,306 L653,318 C600,350 510,358 410,336 C270,300 130,282 0,314 Z"/>
      <path fill="var(--steel-blue)" d="M0,318 C130,288 270,304 410,340 C510,362 600,354 653,322 L653,356 L0,356 Z"/>
    </svg>
    <p class="website">www.branleysteel.com</p>
  </section>

</main>
</body>
</html>
```